TalkBloom - Language Coaching Services

Sleek, innovative, trendy design for Language Coaching business.

TalkBloom is a new UK based company that provides Language Coaching services. We offer highly personalized on-line and face to face language courses. We also impart learning techniques workshops based on the latest neuroscience research for second-language acquisition.

Target Market(s)

Industry/Entity Type

Consulting

Contact Information for Business Card

TalkBloom
DaniraQT@talkbloom.co.uk
TalkBloom.co.uk
London, UK

Font styles to use
Sans Serif

```html
<!DOCTYPE html>
<html lang="en">
<head>
<meta charset="utf-8">
<title>TalkBloom Business Cards</title>
<link href="https://fonts.googleapis.com/css2?family=Oswald:wght@500&family=Work+Sans:wght@300;400&display=swap" rel="stylesheet">
<style>
  :root {
    --backdrop: #1a1a1a;
    --card: #1f1f1f;
    --card-edge: #2a2a2a;
    --foil: #d9d9d9;
    --foil-soft: #a8a8a8;
    --emboss: #141414;
    --emboss-light: #343434;
  }
  * { margin: 0; padding: 0; box-sizing: border-box; }
  html, body {
    width: 1200px; height: 900px; overflow: hidden;
    background: var(--backdrop);
  }
  .canvas {
    position: relative; width: 1200px; height: 900px;
    display: flex; flex-direction: column; align-items: center; justify-content: center; gap: 40px;
  }
  .card {
    position: relative; width: 640px; height: 366px;
    background: linear-gradient(135deg, var(--card) 0%, #232323 60%, #2b2b2b 100%);
    border: 1px solid var(--card-edge);
    box-shadow: 0 14px 30px rgba(0,0,0,0.5);
    font-family: "Work Sans", sans-serif;
  }
  /* Front */
  .card-front {
    display: flex; flex-direction: column; align-items: center; justify-content: center;
  }
  .brand-mark {
    width: 110px; height: 110px; border-radius: 50%;
    border: 4px solid var(--foil-soft);
    margin-bottom: 18px;
  }
  .brand-name {
    font-weight: 300; font-size: 46px; letter-spacing: 4px;
    color: var(--foil); text-transform: uppercase;
  }
  .front-web {
    margin-top: 30px; font-size: 15px; letter-spacing: 1.5px; color: var(--foil-soft);
  }
  /* Back */
  .card-back { padding: 0 60px; }
  .identity {
    position: absolute; left: 60px; top: 112px; width: 250px; text-align: right;
  }
  .person-name {
    font-family: "Oswald", sans-serif; font-weight: 500; font-size: 38px;
    letter-spacing: 1px; text-transform: uppercase; color: var(--emboss);
    text-shadow: 1px 1px 0 var(--emboss-light), -1px -1px 0 #0c0c0c;
    line-height: 1;
  }
  .person-role {
    margin-top: 6px; font-size: 15px; color: var(--emboss);
    text-shadow: 1px 1px 0 var(--emboss-light);
  }
  .divider {
    position: absolute; left: 335px; top: 108px; width: 1px; height: 78px;
    background: var(--foil-soft);
  }
  .contact-list {
    position: absolute; left: 360px; top: 106px; list-style: none;
  }
  .contact-item {
    display: flex; align-items: center; gap: 10px;
    font-size: 17px; letter-spacing: 1px; color: var(--foil); line-height: 26px;
  }
  .contact-item svg { width: 12px; height: 12px; flex: none; }
  .address {
    position: absolute; left: 0; right: 0; bottom: 56px; text-align: center;
    font-size: 16px; letter-spacing: 1.5px; color: var(--foil-soft);
  }
</style>
</head>
<body>
<main class="canvas">
  <section class="card card-front">
    <div class="brand-mark"></div>
    <h1 class="brand-name">TalkBloom</h1>
    <p class="front-web">www.talkbloom.co.uk</p>
  </section>

  <section class="card card-back">
    <div class="identity">
      <h2 class="person-name">Arlo Fenwick</h2>
      <p class="person-role">Director</p>
    </div>
    <div class="divider"></div>
    <ul class="contact-list">
      <li class="contact-item">
        <svg viewBox="0 0 12 12" fill="none" stroke="#a8a8a8" stroke-width="1.4"><path d="M2.5 1.5l2 0.5 0.6 2.4-1.3 1a6 6 0 0 0 2.8 2.8l1-1.3 2.4 0.6 0.5 2c-4.5 0.6-8.6-3.5-8-8z"/></svg>
        (514) 555-0172
      </li>
      <li class="contact-item">
        <svg viewBox="0 0 12 12" fill="none" stroke="#a8a8a8" stroke-width="1.2"><rect x="1" y="2.5" width="10" height="7"/><path d="M1 2.5l5 4 5-4"/></svg>
        Info@talkbloom.co.uk
      </li>
      <li class="contact-item">
        <svg viewBox="0 0 12 12" fill="none" stroke="#a8a8a8" stroke-width="1.1"><circle cx="6" cy="6" r="5"/><ellipse cx="6" cy="6" rx="2.2" ry="5"/><path d="M1 6h10"/></svg>
        www.talkbloom.co.uk
      </li>
    </ul>
    <p class="address">48b Harlow Street, London, UK, 8021</p>
  </section>
</main>
</body>
</html>
```